Quiet Harbor Hours Podcast Artwork

I need a cover for my podcast Quiet Harbor Hours that is clean, modern, and minimalist, but not too feminine

Target Market(s)

People struggling with fertility particularly women who are between the ages of 35-45 though there is a small set of listeners who are men

Requirements
Must have
• Embryo in the Zero
Should not have
• No script text

```html
<!DOCTYPE html>
<html lang="en">
<head>
<meta charset="utf-8">
<title>Quiet Harbor Hours Podcast – Cover Artwork</title>
<link rel="stylesheet" href="https://fonts.googleapis.com/css2?family=Tenor+Sans&display=swap">
<style>
  :root {
    --board: #c3b59b;
    --tile-light: #ffffff;
    --tile-mist: #ececed;
    --wave-deep: #342f38;
    --wave-soft: #4a3f4a;
    --ink: #3a3340;
    --ink-dark: #1f1b22;
  }
  * { margin: 0; padding: 0; box-sizing: border-box; }
  html, body {
    width: 1200px;
    height: 545px;
    overflow: hidden;
    background: var(--board);
  }
  .board {
    position: relative;
    width: 1200px;
    height: 545px;
    background: var(--board);
  }
  .cover {
    position: absolute;
    overflow: hidden;
    background: linear-gradient(135deg, var(--tile-light) 0%, #f6f6f7 45%, var(--tile-mist) 100%);
    box-shadow: 0 8px 10px -6px rgba(60, 50, 40, 0.45);
    container-type: inline-size;
  }
  .cover--hero { left: 51px; top: 64px; width: 417px; height: 417px; }
  .cover--thumb { width: 200px; height: 200px; }
  .cover--r1 { top: 64px; }
  .cover--r2 { top: 282px; }
  .cover--c1 { left: 503px; }
  .cover--c2 { left: 720px; }
  .cover--c3 { left: 941px; }

  .cover__waves {
    position: absolute;
    inset: 0;
    width: 100%;
    height: 100%;
  }
  .wave--deep { fill: var(--wave-deep); }
  .wave--soft { fill: var(--wave-soft); }

  .cover__title {
    position: absolute;
    left: 0;
    right: 0;
    text-align: center;
    font-family: "Tenor Sans", sans-serif;
    color: var(--ink);
    line-height: 1;
  }
  .cover__name {
    display: block;
    font-size: 9.2cqw;
    letter-spacing: -0.01em;
  }
  .cover__label {
    display: block;
    margin-top: 1.2cqw;
    font-size: 4.9cqw;
    letter-spacing: 0.22em;
    color: var(--ink-dark);
  }
  .cover--hero .cover__title { top: 47%; }
  .cover--thumb .cover__title { top: 43%; }
  .cover--thumb .cover__label { margin-top: 0.8cqw; font-size: 5.6cqw; }
</style>
</head>
<body>
<svg width="0" height="0" style="position:absolute" aria-hidden="true">
  <defs>
    <symbol id="cover-waves" viewBox="0 0 100 100" preserveAspectRatio="none">
      <path class="wave--deep" d="M0 0 H51 C51 10 46 16 38 19 C28 23 24 28 20 33 C16 37 10 38 0 36 Z"/>
      <path class="wave--soft" d="M0 34 C8 33 12 27 17 22 C23 15 31 12 38 8 C43 5 46 2 47 0 H51 C51 10 46 16 38 19 C28 23 24 28 20 33 C16 37 10 38 0 36 Z"/>
      <path class="wave--deep" d="M100 70 C95 71 91 68 88 66 C82 61 76 62 73 71 C70 81 63 89 52 100 H100 Z"/>
      <path class="wave--soft" d="M100 70 C95 71 91 68 88 66 C82 61 76 62 73 71 C72 76 70 80 67 84 C73 80 77 74 81 72 C86 70 91 74 96 75 C98 75 99 74 100 74 Z"/>
    </symbol>
  </defs>
</svg>

<main class="board">
  <article class="cover cover--hero">
    <svg class="cover__waves" aria-hidden="true"><use href="#cover-waves"/></svg>
    <h1 class="cover__title">
      <span class="cover__name">Quiet Harbor Hours</span>
      <span class="cover__label">PODCAST</span>
    </h1>
  </article>

  <article class="cover cover--thumb cover--r1 cover--c1">
    <svg class="cover__waves" aria-hidden="true"><use href="#cover-waves"/></svg>
    <p class="cover__title"><span class="cover__name">Quiet Harbor Hours</span><span class="cover__label">PODCAST</span></p>
  </article>
  <article class="cover cover--thumb cover--r1 cover--c2">
    <svg class="cover__waves" aria-hidden="true"><use href="#cover-waves"/></svg>
    <p class="cover__title"><span class="cover__name">Quiet Harbor Hours</span><span class="cover__label">PODCAST</span></p>
  </article>
  <article class="cover cover--thumb cover--r1 cover--c3">
    <svg class="cover__waves" aria-hidden="true"><use href="#cover-waves"/></svg>
    <p class="cover__title"><span class="cover__name">Quiet Harbor Hours</span><span class="cover__label">PODCAST</span></p>
  </article>
  <article class="cover cover--thumb cover--r2 cover--c1">
    <svg class="cover__waves" aria-hidden="true"><use href="#cover-waves"/></svg>
    <p class="cover__title"><span class="cover__name">Quiet Harbor Hours</span><span class="cover__label">PODCAST</span></p>
  </article>
  <article class="cover cover--thumb cover--r2 cover--c2">
    <svg class="cover__waves" aria-hidden="true"><use href="#cover-waves"/></svg>
    <p class="cover__title"><span class="cover__name">Quiet Harbor Hours</span><span class="cover__label">PODCAST</span></p>
  </article>
  <article class="cover cover--thumb cover--r2 cover--c3">
    <svg class="cover__waves" aria-hidden="true"><use href="#cover-waves"/></svg>
    <p class="cover__title"><span class="cover__name">Quiet Harbor Hours</span><span class="cover__label">PODCAST</span></p>
  </article>
</main>
</body>
</html>
```